Business Card

I need a business card for a nutrition/fitness consultant. We are a personalized and online service that caters to developing individual plans based on persons needs. I will send you information to need on card as well as logo. Last business card was grey background and writing was black and red. I think a pic on the backside (maybe a photo that is on the app) would be good?

HelloMarlo (Ill send you logo)
Marlo Venti, Registered Nurse and Certified Sports Nutrionist (R.N., C.S.N.)
Personalized Nutrition and Fitness Architecture

1-800-555-0147 office
(305) 555-0182 cell
website www.hellomarlo-demo.com
marlo@hellomarlo-demo.com

Two locations so maybe two cards
2180 Willowbend Lane, inside Sunpeak Glow Studio
Palm Crescent, Fl 33199

and
7300 W Orchard Parkway
Harbor Point, Florida 33498

Requirements
Must have
• I guess the logo we provide so it is consistent with the new website etc

```html
<!DOCTYPE html>
<html lang="en">
<head>
<meta charset="utf-8">
<title>HelloMarlo – Business Card</title>
<link rel="stylesheet" href="https://fonts.googleapis.com/css2?family=Open+Sans:wght@400;700&display=swap">
<style>
  :root {
    --stage-center: #555555;
    --stage-mid: #2e2e2e;
    --stage-edge: #050505;
    --card-white: #ffffff;
    --ink: #1c1c1c;
    --brand-red: #e31b23;
    --deep-red: #8e0b12;
    --darkest-red: #5a050a;
    --swoosh: #2a2a2a;
    --on-red: #ffffff;
  }
  * { margin: 0; padding: 0; box-sizing: border-box; }
  html, body { width: 1200px; height: 999px; overflow: hidden; }
  body {
    background: radial-gradient(ellipse 620px 600px at 600px 500px, var(--stage-center) 0%, var(--stage-mid) 60%, var(--stage-edge) 100%);
    font-family: "Open Sans", Arial, sans-serif;
    position: relative;
  }
  .card {
    position: absolute;
    left: 230px;
    width: 762px;
    height: 434px;
    overflow: hidden;
  }
  .card--front { top: 69px; background: var(--card-white); }
  .card--back { top: 519px; height: 435px; }

  .front-shape { position: absolute; left: 0; top: 0; width: 762px; height: 434px; }

  .brand {
    position: absolute;
    left: 30px; top: 112px;
    width: 270px;
    display: flex; align-items: center; justify-content: center; gap: 10px;
  }
  .brand__dot { width: 18px; height: 18px; border-radius: 50%; background: var(--brand-red); }
  .brand__name { font-size: 46px; font-weight: 700; color: var(--ink); letter-spacing: -0.5px; line-height: 1; }

  .tagline {
    position: absolute; left: 24px; top: 191px; width: 262px;
    text-align: center; font-size: 18px; line-height: 26px; color: var(--ink);
  }
  .credentials {
    position: absolute; left: 464px; top: 91px;
    font-size: 18px; line-height: 25px; color: var(--ink);
  }
  .address {
    position: absolute; left: 49px; top: 330px;
    font-size: 18px; line-height: 26px; color: var(--on-red);
  }
  .contacts {
    position: absolute; left: 426px; top: 300px;
    list-style: none; color: var(--on-red); font-size: 18px; line-height: 25.5px;
  }
  .contacts li { display: flex; align-items: center; }
  .contacts svg { width: 20px; height: 18px; margin-right: 26px; flex: none; }

  .back-photo {
    position: absolute; inset: 0;
    background: radial-gradient(ellipse 420px 320px at 420px 220px, #c9a07f 0%, #9c6148 30%, var(--deep-red) 65%, var(--darkest-red) 100%);
  }
  .app-shot {
    position: absolute; left: 531px; top: 34px; width: 189px; height: 286px;
    background: var(--card-white); border-radius: 16px; padding: 6px;
  }
  .app-shot__image {
    width: 100%; height: 100%; border-radius: 12px;
    background: linear-gradient(160deg, #d8d8d8 0%, #9a9a9a 55%, #e8e8e8 100%);
  }
</style>
</head>
<body>
  <section class="card card--front">
    <svg class="front-shape" viewBox="0 0 762 434" aria-hidden="true">
      <defs>
        <linearGradient id="redBand" x1="0" y1="0" x2="0" y2="1">
          <stop offset="0" stop-color="#e8202a"/>
          <stop offset="0.45" stop-color="#b5121a"/>
          <stop offset="1" stop-color="#6e060c"/>
        </linearGradient>
      </defs>
      <path d="M0 293 C230 292 500 250 762 176 L762 434 L0 434 Z" fill="url(#redBand)"/>
      <path d="M262 269 C420 262 600 212 762 150 L762 172 C600 222 430 262 262 269 Z" fill="var(--swoosh)"/>
    </svg>

    <div class="brand">
      <span class="brand__name">HelloMarlo</span>
      <span class="brand__dot"></span>
    </div>
    <p class="tagline">Personalized Nutrition<br>and Fitness Architecture</p>
    <p class="credentials">Marlo Venti, Registered Nurse<br>and Certified Sports Nutrionist<br>(R.N., C.S.N.)</p>

    <p class="address">2180 Willowbend Lane, inside<br>Sunpeak Glow Studio<br>Palm Crescent, Fl 33199</p>

    <ul class="contacts">
      <li><svg viewBox="0 0 20 18"><path d="M7 1 L9 5 L7.5 6.5 C8.5 9.5 10 11 12.5 12 L14 10.5 L17 13 L15 16 C9 16 4 10 4 3 Z" fill="#fff"/></svg>1-800-555-0147 office</li>
      <li><svg viewBox="0 0 20 18"><rect x="4" y="1" width="12" height="16" rx="2" fill="#fff"/><path d="M7 13 L13 6" stroke="#a80f17" stroke-width="2"/></svg>(555) 555-0182 cell</li>
      <li><svg viewBox="0 0 20 18"><g fill="none" stroke="#fff" stroke-width="1.4"><circle cx="10" cy="9" r="8"/><ellipse cx="10" cy="9" rx="3.5" ry="8"/><path d="M2 9 H18 M3.5 5 H16.5 M3.5 13 H16.5"/></g></svg>www.hellomarlo-demo.com</li>
      <li><svg viewBox="0 0 20 18"><rect x="1" y="4" width="18" height="11" fill="#fff"/><path d="M1 4 L10 11 L19 4" fill="none" stroke="#a80f17" stroke-width="1.3"/></svg>marlo@hellomarlo-demo.com</li>
    </ul>
  </section>

  <section class="card card--back">
    <div class="back-photo" role="img" aria-label="Portrait photograph of the consultant against a deep red backdrop"></div>
    <div class="app-shot">
      <div class="app-shot__image" role="img" aria-label="Black and white app screenshot of the consultant holding red apples"></div>
    </div>
  </section>
</body>
</html>
```